Riverstone & Pine Construction and Developments business cards

A business card with watermark background (construction work)

Company logo attached

Home improvement projects
House renovations
Bathroom and kitchen renovations
House extensions
New builds and granny flats

Director Omar Haddine
(Phone number)
omar@rpcbuildgroup.com.au
(Instagram logo) rpc_buildgroup

```html
<!DOCTYPE html>
<html lang="en">
<head>
<meta charset="utf-8">
<title>Riverstone &amp; Pine Construction and Developments – Business Cards</title>
<link href="https://fonts.googleapis.com/css2?family=Roboto:wght@400;500&family=Fira+Sans+Condensed:wght@600&display=swap" rel="stylesheet">
<style>
  :root {
    --stage: #2b2b2c;
    --brand-blue: #0a74ba;
    --brand-blue-deep: #0862a0;
    --band-grey: #3d4348;
    --paper: #f8f8f8;
    --ink: #2d2d2d;
    --white: #ffffff;
  }
  * { box-sizing: border-box; margin: 0; padding: 0; }
  html, body {
    width: 1138px; height: 1200px; overflow: hidden;
    background: var(--stage);
    font-family: "Roboto", Arial, sans-serif;
  }
  .card {
    position: absolute;
    border-radius: 16px;
    overflow: hidden;
    text-align: center;
  }
  /* Front */
  .card-front {
    left: 166px; top: 288px; width: 376px; height: 622px;
    background: var(--brand-blue);
    color: var(--white);
  }
  .watermark {
    position: absolute; inset: 0 0 47px 0;
    background: radial-gradient(ellipse at 40% 30%, rgba(255,255,255,0.06), rgba(0,0,0,0) 60%),
                linear-gradient(160deg, var(--brand-blue) 0%, var(--brand-blue-deep) 100%);
  }
  .company-name {
    position: absolute; left: 0; right: 0;
    font-family: "Roboto", Arial, sans-serif;
    font-weight: 500;
    line-height: 1.15;
  }
  .card-front .company-name { top: 130px; font-size: 30px; color: var(--white); }
  .company-name .sub { display: block; font-size: 16px; letter-spacing: 3px; margin-top: 10px; }
  .services { position: absolute; left: 0; right: 0; top: 368px; list-style: none; font-size: 16px; }
  .services li { height: 32px; line-height: 26px; }
  .services .ruled span { display: inline-block; padding: 0 8px; border-bottom: 1.5px solid var(--white); }
  .social {
    position: absolute; left: 0; right: 0;
    font-size: 16px;
    display: flex; justify-content: center; align-items: center; gap: 9px;
  }
  .social .dot { width: 14px; height: 14px; border: 2px solid currentColor; border-radius: 50%; }
  .card-front .social { top: 516px; }
  .web-band {
    position: absolute; left: 0; right: 0; bottom: 0; height: 47px;
    background: var(--band-grey);
    line-height: 47px; font-size: 16px;
  }
  /* Back */
  .card-back {
    left: 604px; top: 290px; width: 373px; height: 620px;
    background: var(--paper);
    color: var(--ink);
  }
  .card-back .company-name { top: 92px; font-size: 30px; color: var(--brand-blue); }
  .person-name {
    position: absolute; left: 0; right: 0; top: 328px;
    font-family: "Fira Sans Condensed", Arial, sans-serif; font-weight: 600;
    font-size: 26px; color: var(--brand-blue);
  }
  .person-role { position: absolute; left: 0; right: 0; top: 362px; font-size: 16px; }
  .contact-icons { position: absolute; left: 0; right: 0; top: 406px; display: flex; justify-content: center; }
  .contact-list { position: absolute; left: 0; right: 0; top: 450px; list-style: none; font-size: 16px; line-height: 24px; }
  .contact-list .accent { color: var(--brand-blue); }
  .card-back .social { top: 538px; }
  .card-back .social .dot { color: var(--brand-blue); }
</style>
</head>
<body>

<section class="card card-front">
  <div class="watermark" role="img" aria-label="Faint construction site watermark"></div>
  <h1 class="company-name">Riverstone &amp; Pine<span class="sub">CONSTRUCTION AND DEVELOPMENTS</span></h1>
  <ul class="services">
    <li class="ruled"><span>Home Improvement Projects</span></li>
    <li class="ruled"><span>Bathroom &amp; Kitchen Renovations</span></li>
    <li class="ruled"><span>New Builds &amp; Granny Flats</span></li>
    <li>House Renovations &nbsp;|&nbsp; House Extensions</li>
  </ul>
  <p class="social"><span class="dot"></span>rpc_buildgroup</p>
  <p class="web-band">www.rpcbuildgroup.com.au</p>
</section>

<section class="card card-back">
  <h1 class="company-name">Riverstone &amp; Pine<span class="sub">CONSTRUCTION AND DEVELOPMENTS</span></h1>
  <h2 class="person-name">Omar Haddine</h2>
  <p class="person-role">Managing Director</p>
  <div class="contact-icons">
    <svg width="260" height="26" viewBox="0 0 260 26" aria-hidden="true">
      <g fill="none" stroke="#0a74ba" stroke-width="1.8">
        <line x1="0" y1="13" x2="48" y2="13" stroke="#2d2d2d" stroke-width="2"/>
        <line x1="212" y1="13" x2="260" y2="13" stroke="#2d2d2d" stroke-width="2"/>
        <circle cx="103" cy="13" r="11.5"/>
        <circle cx="130" cy="13" r="11.5"/>
        <circle cx="157" cy="13" r="11.5"/>
        <circle cx="157" cy="13" r="6"/>
        <ellipse cx="157" cy="13" rx="2.6" ry="6"/>
        <line x1="151" y1="13" x2="163" y2="13"/>
      </g>
      <path d="M97 9 h12 l-1.5 3 h-9 z M98 12.5 h10 v5 h-10 z" fill="#0a74ba"/>
      <rect x="124" y="9" width="12" height="8.5" fill="#0a74ba"/>
      <path d="M124 9 l6 5 l6 -5" fill="none" stroke="#f8f8f8" stroke-width="1.3"/>
    </svg>
  </div>
  <ul class="contact-list">
    <li>0412 384 907</li>
    <li>omar@rpcbuildgroup.com.au</li>
    <li>www.<span class="accent">rpcbuildgroup</span>.com.au</li>
  </ul>
  <p class="social"><span class="dot"></span>rpc_buildgroup</p>
</section>

</body>
</html>
```